PowerPoint template for my training workshop business

I would like to have a PowerPoint template created using my logo and palette materials created by Brivantelox. I train and facilitate workshops using PowerPoint in both corporate and public settings.

I have attached the original design elements to this request.

```html
<!DOCTYPE html>
<html lang="en">
<head>
<meta charset="utf-8">
<title>Marisol Kettner Coaching – Presentation Template</title>
<link href="https://fonts.googleapis.com/css2?family=Cinzel:wght@400;600;700&family=Lato:wght@300;400;700&display=swap" rel="stylesheet">
<style>
:root{
  --orange:#f7941d;
  --orange-light:#fbb33a;
  --orange-deep:#f28a13;
  --ink:#4a4a4a;
  --muted:#9a9a9a;
  --faint:#c4c4c4;
  --page:#f1f1f1;
  --white:#ffffff;
}
*{box-sizing:border-box;margin:0;padding:0}
html,body{width:1200px;height:3566px;overflow:hidden}
body{background:var(--page);position:relative;font-family:"Lato",sans-serif;color:var(--ink)}
.hero{position:absolute;left:200px;top:70px;width:800px;height:450px;background:var(--white);box-shadow:0 10px 40px rgba(0,0,0,.08);overflow:hidden}
.slide{position:absolute;width:587px;height:330px;background:var(--white);overflow:hidden}
.col-l{left:10px}.col-r{left:605px}
.photo{position:absolute}
.heading{font-family:"Cinzel",serif;font-weight:400;color:var(--ink);letter-spacing:.5px;line-height:1.15}
.sub{font-family:"Lato",sans-serif;font-weight:300;color:var(--muted)}
.small{font-size:8px;font-weight:300;color:var(--faint);line-height:1.45}
.brand{position:absolute;display:flex;align-items:center;gap:7px;font-family:"Cinzel",serif;font-weight:600;color:var(--orange);white-space:nowrap}
.brand .dot{border-radius:50%;border:2px solid var(--orange);flex:none}
.brand.sm{font-size:8px}.brand.sm .dot{width:16px;height:16px}
.brand.md{font-size:13px}.brand.md .dot{width:26px;height:26px;border-width:3px}
.brand.white{color:var(--white)}.brand.white .dot{border-color:var(--white)}
.corner{top:18px;right:18px}
.pill{position:absolute;background:var(--orange);color:var(--white);font-size:8px;padding:2px 7px;border-radius:2px}
.mark{position:absolute;border-radius:50%;background:radial-gradient(circle at 40% 40%,#fff 0 30%,var(--orange-light) 31% 60%,var(--orange-deep) 61%)}
.num{position:absolute;width:26px;height:26px;border-radius:50%;background:var(--orange);color:var(--white);font-family:"Cinzel",serif;font-size:11px;display:flex;align-items:center;justify-content:center}
.item-title{position:absolute;font-family:"Cinzel",serif;font-size:9.5px;color:var(--ink)}
.item-text{position:absolute;width:190px}
.on-orange{color:var(--white)}
.icon{position:absolute}
.stat{position:absolute;color:var(--white);text-align:center;width:90px}
.stat b{display:block;font-family:"Cinzel",serif;font-weight:400;font-size:22px}
.stat span{font-size:7px;letter-spacing:.5px}
.ring{position:absolute;width:14px;height:14px;border-radius:50%;border:2px solid var(--orange)}
.quote-mark{position:absolute;font-family:"Cinzel",serif;font-weight:700;color:var(--orange);font-size:90px;line-height:1}
.center{text-align:center}
</style>
</head>
<body>

<!-- Featured title slide -->
<section class="hero" aria-label="Title slide">
  <div class="photo" role="img" aria-label="Photo of the smiling coach resting her chin on her hand" style="left:400px;top:0;width:400px;height:450px;background:linear-gradient(90deg,#fff 0%,#efe7df 35%,#d9c7b6 70%,#c9b29c 100%)"></div>
  <div class="brand md" style="left:60px;top:130px"><span class="dot"></span>MARISOL KETTNER</div>
  <h1 class="heading" style="position:absolute;left:60px;top:190px;font-size:28px">COACHING PRESENTATION</h1>
  <p class="sub" style="position:absolute;left:60px;top:232px;font-size:16px">Subtitle of your coaching presentation title</p>
  <span class="pill" style="left:60px;top:272px;font-size:10px">Saturday May 9 , 2020</span>
</section>

<!-- Row 1 -->
<section class="slide col-l" style="top:782px" aria-label="Title slide with photo">
  <div class="photo" role="img" aria-label="Photo of the coach smiling at her desk" style="left:290px;top:0;width:297px;height:330px;background:linear-gradient(90deg,#fff 0%,#eee4da 40%,#d6c2ae 100%)"></div>
  <div class="brand sm" style="left:45px;top:100px;font-size:11px"><span class="dot" style="width:22px;height:22px"></span>MARISOL KETTNER</div>
  <h2 class="heading" style="position:absolute;left:45px;top:160px;font-size:17px">COACHING PRESENTATION</h2>
  <p class="sub" style="position:absolute;left:45px;top:186px;font-size:11px">Subtitle of your coaching presentation title</p>
  <span class="pill" style="left:45px;top:220px">Saturday May 9 , 2020</span>
</section>

<section class="slide col-r" style="top:782px" aria-label="Title slide orange">
  <svg width="587" height="330" style="position:absolute;left:0;top:0"><defs><linearGradient id="og" x1="0" y1="0" x2="1" y2="1"><stop offset="0" stop-color="#fbb33a"/><stop offset="1" stop-color="#f28a13"/></linearGradient></defs><path d="M165 0 C300 80 300 250 165 330 L587 330 L587 0Z" fill="url(#og)"/></svg>
  <div class="mark" style="left:28px;top:80px;width:165px;height:165px"></div>
  <div class="brand sm white" style="left:285px;top:100px;font-size:11px"><span class="dot" style="width:22px;height:22px"></span>MARISOL KETTNER</div>
  <h2 class="heading on-orange" style="position:absolute;left:285px;top:155px;font-size:17px">COACHING PRESENTATION</h2>
  <p class="sub on-orange" style="position:absolute;left:285px;top:181px;font-size:11px">Subtitle of your coaching presentation title</p>
  <span class="pill" style="left:285px;top:213px;background:#fff;color:var(--orange)">Saturday May 9 , 2020</span>
</section>

<!-- Row 2 -->
<section class="slide col-l" style="top:1120px" aria-label="Agenda">
  <div class="brand sm corner"><span class="dot"></span>MARISOL KETTNER</div>
  <h2 class="heading" style="position:absolute;left:24px;top:26px;font-size:12px">COACHING AGENDA</h2>
  <div class="num" style="left:42px;top:86px">01</div><div class="item-title" style="left:90px;top:82px">ABOUT MARISOL KETTNER</div><p class="item-text small" style="left:90px;top:96px">Short note on this topic and its key outcome.</p>
  <div class="num" style="left:42px;top:163px">02</div><div class="item-title" style="left:90px;top:159px">PMP MASTERY PROGRAM</div><p class="item-text small" style="left:90px;top:173px">Short note on this topic and its key outcome.</p>
  <div class="num" style="left:42px;top:240px">03</div><div class="item-title" style="left:90px;top:236px">BUSINESS COACHING</div><p class="item-text small" style="left:90px;top:250px">Short note on this topic and its key outcome.</p>
  <div class="num" style="left:315px;top:86px">04</div><div class="item-title" style="left:363px;top:82px">BUSINESS COACHING PROGRAM</div><p class="item-text small" style="left:363px;top:96px">Short note on this topic and its key outcome.</p>
  <div class="num" style="left:315px;top:163px">05</div><div class="item-title" style="left:363px;top:159px">SELF IMPROVEMENT</div><p class="item-text small" style="left:363px;top:173px">Short note on this topic and its key outcome.</p>
  <div class="num" style="left:315px;top:240px">06</div><div class="item-title" style="left:363px;top:236px">TRAINING DEVELOPMENT</div><p class="item-text small" style="left:363px;top:250px">Short note on this topic and its key outcome.</p>
</section>

<section class="slide col-r" style="top:1120px" aria-label="Our coach">
  <svg width="587" height="330" style="position:absolute;left:0;top:0"><path d="M0 0 L180 0 C260 90 260 250 205 330 L0 330Z" fill="url(#og)"/></svg>
  <div class="photo" role="img" aria-label="Portrait photo of the coach" style="left:20px;top:45px;width:200px;height:285px;border-radius:100px 100px 0 0;background:linear-gradient(180deg,#5a3a2c 0%,#8a6a58 45%,#4e4238 100%)"></div>
  <div class="brand sm corner"><span class="dot"></span>MARISOL KETTNER</div>
  <svg class="icon" style="left:300px;top:120px" width="12" height="18" viewBox="0 0 12 18"><rect x="3" y="0" width="6" height="11" rx="3" fill="#f7941d"/><path d="M1 8a5 5 0 0 0 10 0M6 13v4" stroke="#f7941d" stroke-width="1.5" fill="none"/></svg>
  <div class="heading" style="position:absolute;left:330px;top:123px;font-size:9px;color:var(--orange)">OUR COACH</div>
  <h2 class="heading" style="position:absolute;left:303px;top:153px;font-size:22px">MARISOL KETTNER</h2>
  <p class="sub" style="position:absolute;left:303px;top:188px;font-size:13px">Founder of Marisol Kettner Coaching</p>
</section>

<!-- Row 3 -->
<section class="slide col-l" style="top:1458px" aria-label="About the coach">
  <svg width="587" height="330" style="position:absolute;left:0;top:0"><path d="M587 0 L420 0 C330 60 320 260 380 330 L587 330Z" fill="url(#og)"/></svg>
  <div class="photo" role="img" aria-label="Portrait photo of the coach" style="left:380px;top:55px;width:200px;height:275px;border-radius:100px 100px 0 0;background:linear-gradient(180deg,#5a3a2c 0%,#8a6a58 45%,#4e4238 100%)"></div>
  <div class="brand sm" style="left:66px;top:75px;font-size:11px"><span class="dot" style="width:22px;height:22px"></span>MARISOL KETTNER</div>
  <h2 class="heading" style="position:absolute;left:66px;top:135px;font-size:21px">ABOUT MARISOL</h2>
  <p class="sub" style="position:absolute;left:66px;top:172px;width:245px;font-size:12px;line-height:1.6">Lorem ipsum dolor sitame consectetuer adipiscing elit. Maecenas porti congue massa. Fusce posuere, magna pulvin ultricies purus lectus.</p>
</section>

<section class="slide col-r" style="top:1458px" aria-label="Join our program">
  <div class="photo" role="img" aria-label="Faint photo of a workshop audience" style="left:0;top:0;width:587px;height:330px;background:linear-gradient(180deg,#f7f5f3,#fff 60%)"></div>
  <div class="brand md" style="left:183px;top:82px"><span class="dot"></span>MARISOL KETTNER</div>
  <h2 class="heading center" style="position:absolute;left:0;width:587px;top:170px;font-size:27px"><span style="color:var(--orange)">LET'S JOIN</span> OUR PROGRAM</h2>
  <p class="sub center" style="position:absolute;left:80px;width:427px;top:215px;font-size:10px;line-height:1.7">Lorem ipsum dolor sit ametaeo mang consectetuer adipiscing porttitor congue ngumbe es teh mangan sego trus wareg.</p>
</section>

<!-- Row 4 -->
<section class="slide col-l" style="top:1796px" aria-label="Next coaching program">
  <div class="photo" role="img" aria-label="Photo of a woman presenting and pointing" style="left:0;top:0;width:250px;height:330px;background:linear-gradient(90deg,#e8e2dc 0%,#d8cdc3 50%,#fff 100%)"></div>
  <div style="position:absolute;left:0;top:0;width:48px;height:90px;background:var(--orange-deep)"></div>
  <div class="brand sm corner"><span class="dot"></span>MARISOL KETTNER</div>
  <h2 class="heading" style="position:absolute;left:278px;top:90px;font-size:21px">NEXT COACHING<br>PROGRAM</h2>
  <p class="sub" style="position:absolute;left:278px;top:150px;font-size:11px">Do not miss our next program</p>
  <div style="position:absolute;left:278px;top:195px;width:62px;height:62px;border-radius:50%;background:var(--orange);color:#fff;text-align:center;font-family:'Cinzel',serif;padding-top:13px;font-size:18px;line-height:1">07<br><span style="font-size:9px">JUN</span></div>
  <div class="item-title" style="left:355px;top:198px">THE GREATEST COACHING<br>PROGRAM TITLE</div>
  <p class="item-text small" style="left:355px;top:226px;width:160px">Short note on this topic and its key outcome.</p>
</section>

<section class="slide col-r" style="top:1796px" aria-label="Mission and vision">
  <svg class="icon" style="left:100px;top:100px" width="30" height="30" viewBox="0 0 30 30"><circle cx="15" cy="15" r="12" stroke="#f7941d" stroke-width="2.5" fill="none"/><circle cx="15" cy="15" r="6" stroke="#f7941d" stroke-width="2.5" fill="none"/><circle cx="15" cy="15" r="2" fill="#f7941d"/></svg>
  <h3 class="heading center" style="position:absolute;left:35px;width:160px;top:140px;font-size:17px">MISSION</h3>
  <p class="small center" style="position:absolute;left:45px;width:140px;top:168px">Short note on this topic and its key outcome.</p>
  <div class="mark" style="left:238px;top:85px;width:112px;height:112px"></div>
  <div class="brand md" style="left:222px;top:215px;font-size:14px"><span class="dot" style="display:none"></span>MARISOL KETTNER</div>
  <svg class="icon" style="left:452px;top:102px" width="34" height="24" viewBox="0 0 34 24"><path d="M2 12C9 2 25 2 32 12C25 22 9 22 2 12Z" stroke="#f7941d" stroke-width="2.5" fill="none"/><circle cx="17" cy="12" r="5" fill="#f7941d"/></svg>
  <h3 class="heading center" style="position:absolute;left:390px;width:160px;top:140px;font-size:17px">VISION</h3>
  <p class="small center" style="position:absolute;left:400px;width:140px;top:168px">Short note on this topic and its key outcome.</p>
</section>

<!-- Row 5 -->
<section class="slide col-l" style="top:2134px" aria-label="Coaching program">
  <div class="mark" style="left:107px;top:50px;width:100px;height:100px"></div>
  <h2 class="heading center" style="position:absolute;left:30px;width:260px;top:180px;font-size:19px">MARISOL KETTNER</h2>
  <div class="heading center" style="position:absolute;left:30px;width:260px;top:206px;font-size:14px;color:var(--orange);font-weight:600">COACHING PROGRAM</div>
  <p class="sub center" style="position:absolute;left:60px;width:200px;top:242px;font-size:12px;line-height:1.5">This space for paragraph or subtitle text</p>
  <div class="num" style="left:312px;top:60px">01</div><div class="item-title" style="left:358px;top:56px">BUSINESS COACHING</div><p class="item-text small" style="left:358px;top:70px">Short note on this topic and its key outcome.</p>
  <div class="num" style="left:312px;top:118px">02</div><div class="item-title" style="left:358px;top:114px">SELF IMPROVEMENT</div><p class="item-text small" style="left:358px;top:128px">Short note on this topic and its key outcome.</p>
  <div class="num" style="left:312px;top:176px">03</div><div class="item-title" style="left:358px;top:172px">MANAGEMENT PROGRAM</div><p class="item-text small" style="left:358px;top:186px">Short note on this topic and its key outcome.</p>
  <div class="num" style="left:312px;top:234px">04</div><div class="item-title" style="left:358px;top:230px">SUCCESS TRAINING</div><p class="item-text small" style="left:358px;top:244px">Short note on this topic and its key outcome.</p>
</section>

<section class="slide col-r" style="top:2134px" aria-label="Break slide">
  <div class="photo" role="img" aria-label="Photo of a woman with a cup of coffee" style="left:0;top:0;width:300px;height:330px;background:linear-gradient(90deg,#3f6f8f 0%,#7c97a8 50%,#e9ecee 85%,#fff 100%)"></div>
  <div class="brand sm" style="left:290px;top:100px;font-size:11px"><span class="dot" style="width:22px;height:22px"></span>MARISOL KETTNER</div>
  <h2 class="heading" style="position:absolute;left:290px;top:160px;font-size:20px">LET'S TAKE A BREAK</h2>
  <p class="sub" style="position:absolute;left:290px;top:190px;width:250px;font-size:12px;line-height:1.5">This space for paragraph or subtitle text for break slide.</p>
</section>

<!-- Row 6 -->
<section class="slide col-l" style="top:2472px" aria-label="Facts">
  <svg width="587" height="330" style="position:absolute;left:0;top:0"><path d="M587 0 L410 0 C320 70 320 260 410 330 L587 330Z" fill="url(#og)"/></svg>
  <div class="mark" style="left:124px;top:66px;width:96px;height:96px"></div>
  <h2 class="heading center" style="position:absolute;left:40px;width:265px;top:195px;font-size:19px">MARISOL KETTNER</h2>
  <div class="heading center" style="position:absolute;left:40px;width:265px;top:222px;font-size:14px;color:var(--orange);font-weight:600">THE FACT ABOUT ME</div>
  <p class="sub center" style="position:absolute;left:40px;width:265px;top:250px;font-size:10.5px">Fact About Marisol Kettner Coaching</p>
  <svg class="icon" style="left:420px;top:48px" width="24" height="22" viewBox="0 0 24 22"><path d="M12 21L2 11A5.5 5.5 0 0 1 12 4A5.5 5.5 0 0 1 22 11Z" fill="#fff"/></svg>
  <div class="stat" style="left:467px;top:36px"><b>1748</b><span>HAPPY CLIENTS</span></div>
  <svg class="icon" style="left:420px;top:115px" width="24" height="24" viewBox="0 0 24 24"><path d="M4 20L9 15M14 4C19 4 20 5 20 10L12 18L6 12Z" fill="#fff" stroke="#fff" stroke-width="1.5"/></svg>
  <div class="stat" style="left:467px;top:101px"><b>300+</b><span>PROJECT SUCCESS</span></div>
  <svg class="icon" style="left:420px;top:180px" width="24" height="24" viewBox="0 0 24 24"><rect x="2" y="5" width="20" height="17" rx="2" fill="#fff"/><rect x="6" y="2" width="2" height="5" fill="#fff"/><rect x="16" y="2" width="2" height="5" fill="#fff"/></svg>
  <div class="stat" style="left:467px;top:166px"><b>10</b><span>YEARS EXPERIENCE</span></div>
  <svg class="icon" style="left:420px;top:243px" width="24" height="26" viewBox="0 0 24 26"><circle cx="12" cy="10" r="8" fill="#fff"/><path d="M7 16L5 25L12 21L19 25L17 16" fill="#fff"/></svg>
  <div class="stat" style="left:467px;top:230px"><b>30+</b><span>COACHING<br>AWARD</span></div>
</section>

<section class="slide col-r" style="top:2472px" aria-label="Coaching points">
  <svg width="587" height="330" style="position:absolute;left:0;top:0"><path d="M0 0 L190 0 C270 90 270 250 210 330 L0 330Z" fill="url(#og)"/></svg>
  <div class="mark" style="left:58px;top:72px;width:104px;height:104px;background:radial-gradient(circle at 40% 40%,var(--orange-light) 0 35%,#fff 36% 100%)"></div>
  <h2 class="heading center on-orange" style="position:absolute;left:10px;width:200px;top:200px;font-size:24px">COACHING<br>POINT</h2>
  <div class="icon" style="left:324px;top:40px;width:26px;height:30px;background:var(--orange);border-radius:3px 3px 0 0"></div>
  <div class="item-title center" style="left:272px;width:130px;top:80px">SELF<br>IMPROVEMENT</div><p class="small center" style="position:absolute;left:282px;width:110px;top:106px">Short note on this topic and its key outcome.</p>
  <div class="icon" style="left:473px;top:40px;width:34px;height:30px;background:var(--orange);border-radius:50% 50% 0 0"></div>
  <div class="item-title center" style="left:425px;width:130px;top:80px">PROFESSIONAL<br>SKILLS</div><p class="small center" style="position:absolute;left:435px;width:110px;top:106px">Short note on this topic and its key outcome.</p>
  <div class="icon" style="left:324px;top:175px;width:28px;height:30px;background:var(--orange);border-radius:3px"></div>
  <div class="item-title center" style="left:272px;width:130px;top:213px">BUSINESS<br>COACHING</div><p class="small center" style="position:absolute;left:282px;width:110px;top:239px">Short note on this topic and its key outcome.</p>
  <div class="icon" style="left:475px;top:175px;width:30px;height:30px;background:var(--orange);border-radius:50%"></div>
  <div class="item-title center" style="left:425px;width:130px;top:213px">MANAGEMENT<br>PROGRAM</div><p class="small center" style="position:absolute;left:435px;width:110px;top:239px">Short note on this topic and its key outcome.</p>
</section>

<!-- Row 7 -->
<section class="slide col-l" style="top:2810px" aria-label="Testimonial">
  <div class="brand sm corner"><span class="dot"></span>MARISOL KETTNER</div>
  <div class="photo" role="img" aria-label="Round portrait photo of the quoted person" style="left:251px;top:60px;width:86px;height:86px;border-radius:50%;border:5px solid var(--orange);background:linear-gradient(180deg,#e5ddd5,#6b4a3a)"></div>
  <div class="quote-mark" style="left:88px;top:150px">“</div>
  <p class="heading center" style="position:absolute;left:170px;width:320px;top:168px;font-size:12px;font-weight:600;line-height:1.55">A SUCCESSFULL PEOPLE IS FUSCE POSUERE, MAGNA SED PULVINAR ULTRICIES, PURUS LECTUS MALESUADA</p>
  <div class="heading center" style="position:absolute;left:170px;width:320px;top:240px;font-size:10px;color:var(--orange);font-weight:600">ODILE FENWICK</div>
  <p class="sub center" style="position:absolute;left:170px;width:320px;top:256px;font-size:9px">Vendor of Success Agency</p>
</section>

<section class="slide col-r" style="top:2810px" aria-label="Quotes today">
  <div class="brand sm corner"><span class="dot"></span>MARISOL KETTNER</div>
  <h2 class="heading center" style="position:absolute;left:0;width:587px;top:78px;font-size:26px">QUOTES TODAY</h2>
  <div class="quote-mark" style="left:88px;top:135px">“</div>
  <p class="heading center" style="position:absolute;left:170px;width:320px;top:150px;font-size:12px;font-weight:600;line-height:1.55">A SUCCESSFULL PEOPLE IS FUSCE POSUERE, MAGNA SED PULVINAR ULTRICIES, PURUS LECTUS MALESUADA</p>
  <div class="heading center" style="position:absolute;left:170px;width:320px;top:222px;font-size:10px;color:var(--orange);font-weight:600">ODILE FENWICK</div>
  <p class="sub center" style="position:absolute;left:170px;width:320px;top:238px;font-size:9px">Vendor of Success Agency</p>
</section>

<!-- Row 8 -->
<section class="slide col-l" style="top:3148px" aria-label="Bullet list">
  <div class="brand sm corner"><span class="dot"></span>MARISOL KETTNER</div>
  <h2 class="heading" style="position:absolute;left:24px;top:26px;font-size:12px">BULLET LIST SLIDE</h2>
  <div class="ring" style="left:24px;top:76px"></div><div class="item-title" style="left:60px;top:76px">HEADING POINT</div><p class="item-text small" style="left:60px;top:90px;width:120px">Short note on this topic and its key outcome.</p>
  <div class="ring" style="left:215px;top:76px"></div><div class="item-title" style="left:251px;top:76px">HEADING POINT</div><p class="item-text small" style="left:251px;top:90px;width:120px">Short note on this topic and its key outcome.</p>
  <div class="ring" style="left:406px;top:76px"></div><div class="item-title" style="left:442px;top:76px">HEADING POINT</div><p class="item-text small" style="left:442px;top:90px;width:120px">Short note on this topic and its key outcome.</p>
  <div class="ring" style="left:24px;top:160px"></div><div class="item-title" style="left:60px;top:160px">HEADING POINT</div><p class="item-text small" style="left:60px;top:174px;width:120px">Short note on this topic and its key outcome.</p>
  <div class="ring" style="left:215px;top:160px"></div><div class="item-title" style="left:251px;top:160px">HEADING POINT</div><p class="item-text small" style="left:251px;top:174px;width:120px">Short note on this topic and its key outcome.</p>
  <div class="ring" style="left:406px;top:160px"></div><div class="item-title" style="left:442px;top:160px">HEADING POINT</div><p class="item-text small" style="left:442px;top:174px;width:120px">Short note on this topic and its key outcome.</p>
  <div class="ring" style="left:24px;top:244px"></div><div class="item-title" style="left:60px;top:244px">HEADING POINT</div><p class="item-text small" style="left:60px;top:258px;width:120px">Short note on this topic and its key outcome.</p>
  <div class="ring" style="left:215px;top:244px"></div><div class="item-title" style="left:251px;top:244px">HEADING POINT</div><p class="item-text small" style="left:251px;top:258px;width:120px">Short note on this topic and its key outcome.</p>
  <div class="ring" style="left:406px;top:244px"></div><div class="item-title" style="left:442px;top:244px">HEADING POINT</div><p class="item-text small" style="left:442px;top:258px;width:120px">Short note on this topic and its key outcome.</p>
</section>

<section class="slide col-r" style="top:3148px;background:linear-gradient(135deg,var(--orange-light),var(--orange-deep))" aria-label="Contact">
  <div class="photo" role="img" aria-label="Round portrait photo of the coach" style="left:253px;top:16px;width:82px;height:82px;border-radius:50%;border:4px solid #fff;background:linear-gradient(180deg,#5a3a2c,#8a6a58)"></div>
  <p class="heading center on-orange" style="position:absolute;left:0;width:587px;top:152px;font-size:9px">HAVE A QUESTION ? JUST GET IN TOUCH</p>
  <h2 class="heading center on-orange" style="position:absolute;left:0;width:587px;top:166px;font-size:28px">CONTACT ME</h2>
  <svg class="icon" style="left:75px;top:218px" width="14" height="18" viewBox="0 0 14 18"><path d="M7 17C2 11 1 9 1 7a6 6 0 0 1 12 0c0 2-1 4-6 10Z" fill="#fff"/><circle cx="7" cy="7" r="2.3" fill="#f7941d"/></svg>
  <div class="on-orange" style="position:absolute;left:106px;top:214px;font-size:9px;line-height:1.4"><span class="heading on-orange" style="font-size:8.5px">MAIN OFFICE</span><br>Fairhaven Valley area</div>
  <svg class="icon" style="left:74px;top:264px" width="16" height="16" viewBox="0 0 16 16"><path d="M3 1l3 3-2 2c1 2 3 4 6 6l2-2 3 3-2 2C7 15 1 9 1 3Z" fill="#fff"/></svg>
  <div class="on-orange" style="position:absolute;left:106px;top:260px;font-size:9px;line-height:1.4"><span class="heading on-orange" style="font-size:8.5px">CALL ME</span><br>555-014-2290</div>
  <svg class="icon" style="left:312px;top:221px" width="16" height="12" viewBox="0 0 16 12"><rect width="16" height="12" rx="1" fill="#fff"/><path d="M1 1l7 6 7-6" stroke="#f7941d" stroke-width="1.4" fill="none"/></svg>
  <div class="on-orange" style="position:absolute;left:343px;top:214px;font-size:9px;line-height:1.4"><span class="heading on-orange" style="font-size:8.5px">EMAIL</span><br>hello@kettnercoaching.example</div>
  <svg class="icon" style="left:312px;top:264px" width="16" height="16" viewBox="0 0 16 16"><circle cx="8" cy="8" r="7" stroke="#fff" stroke-width="1.5" fill="none"/><path d="M1 8h14M8 1c-3 4-3 10 0 14M8 1c3 4 3 10 0 14" stroke="#fff" stroke-width="1.2" fill="none"/></svg>
  <div class="on-orange" style="position:absolute;left:343px;top:260px;font-size:9px;line-height:1.4"><span class="heading on-orange" style="font-size:8.5px">WEBSITE</span><br>www.kettnercoaching.example</div>
</section>

</body>
</html>
```